Create a business promotion flyer to leave in customer mailboxes. We are a bulk petroleum supplier, servicing any industry that requires diesel. Base in griffith NSW, servicing griffith area and surrounds.

Business Name - Terra Petro
Fuel@terrapetro-example.com.au
Marco - 0400 000 001 mtorrisi@terrapetro-example.com.au
Liam - 0400 000 002 lharcourt@terrapetro-example.com.au
Peter - 0400 000 003 pwinslow@terrapetro-example.com.au
Office 02 5550 0100

Bulk Fuel deliveries.
Oils & lubricants
Local Family owned business

```html
<!DOCTYPE html>
<html lang="en">
<head>
<meta charset="utf-8">
<title>Terra Petro – Bulk Fuel Supply Flyer</title>
<link rel="stylesheet" href="https://fonts.googleapis.com/css2?family=Roboto:wght@300;400;500&family=Roboto+Condensed:wght@700&display=swap">
<style>
  :root {
    --red: #e8281e;
    --grey-bar: #6b6b6b;
    --grey-text: #4a4a4a;
    --card: #ececec;
    --ink: #333333;
    --white: #ffffff;
    --stage: #f2f2f2;
  }
  * { box-sizing: border-box; margin: 0; padding: 0; }
  html, body { width: 1200px; height: 850px; overflow: hidden; }
  body { background: var(--stage); font-family: "Roboto", sans-serif; position: relative; }

  .flyer {
    position: absolute; left: 315px; top: 20px;
    width: 570px; height: 810px;
    background: var(--white);
    overflow: hidden;
    box-shadow: 0 6px 24px rgba(0,0,0,.18);
  }
  .brand {
    position: absolute; top: 34px; left: 0; right: 0;
    text-align: center; color: var(--red);
    font-weight: 500; font-size: 24px; line-height: 30px;
  }
  .headline-top {
    position: absolute; top: 100px; left: 0; right: 0; text-align: center;
    font-weight: 300; font-size: 39px; line-height: 46px;
    color: var(--grey-text); letter-spacing: .3px;
  }
  .headline-main {
    position: absolute; top: 146px; left: 0; right: 0; text-align: center;
    font-family: "Roboto Condensed", sans-serif; font-weight: 700; font-size: 61px; line-height: 64px;
    color: var(--red); letter-spacing: .3px;
  }
  .hero { position: absolute; left: 0; top: 0; width: 570px; height: 600px; }

  .service { position: absolute; left: 0; right: 0; height: 40px; }
  .service-bar {
    position: absolute; left: 42px; top: 0; height: 40px; right: 0;
    background: var(--grey-bar); color: var(--white);
    font-family: "Roboto Condensed", sans-serif; font-weight: 700; font-size: 27px;
    line-height: 40px; padding-left: 32px; letter-spacing: .3px;
  }
  .service-icon {
    position: absolute; left: 22px; top: 1px; width: 38px; height: 38px;
    border-radius: 50%; background: var(--red);
    border: 3px solid var(--white);
    box-shadow: 0 0 0 1px rgba(0,0,0,.1);
    display: flex; align-items: center; justify-content: center;
  }
  .service--fuel { top: 448px; }
  .service--fuel .service-bar { right: 84px; }
  .service--oils { top: 494px; }
  .service--family { top: 544px; }

  .cta {
    position: absolute; top: 606px; left: 0; right: 0; text-align: center;
    font-size: 21px; line-height: 26px; color: var(--ink);
  }
  .cta strong { color: var(--red); font-family: "Roboto Condensed", sans-serif; font-weight: 700; }

  .team { position: absolute; top: 661px; left: 0; right: 0; height: 88px; }
  .contact {
    position: absolute; top: 0; width: 164px; height: 88px;
    background: var(--card); border-radius: 5px; text-align: center;
  }
  .contact--marco { left: 24px; }
  .contact--liam { left: 203px; }
  .contact--peter { left: 382px; }
  .contact-name {
    position: absolute; top: -11px; left: 38px; width: 88px; height: 24px;
    background: var(--red); color: var(--white); border-radius: 4px 4px 4px 0;
    font-family: "Roboto Condensed", sans-serif; font-weight: 700; font-size: 19px; line-height: 24px;
  }
  .contact-phone {
    position: absolute; top: 20px; left: 0; right: 0;
    font-family: "Roboto Condensed", sans-serif; font-weight: 700; font-size: 21px; line-height: 26px;
    color: var(--ink); letter-spacing: .5px;
  }
  .contact-email {
    position: absolute; top: 61px; left: 0; right: 0;
    font-size: 8.6px; line-height: 12px; color: var(--ink); white-space: nowrap;
  }

  .footer {
    position: absolute; left: 0; right: 0; top: 761px; height: 49px;
    background: var(--red); color: var(--white);
    line-height: 49px;
  }
  .footer-office { position: absolute; left: 24px; font-size: 20px; }
  .footer-email { position: absolute; right: 20px; font-size: 14.5px; }
  .footer-call {
    position: absolute; left: 256px; top: -20px; width: 59px; height: 59px;
    border-radius: 50%; background: var(--red); border: 4px solid var(--white);
    display: flex; align-items: center; justify-content: center;
  }
</style>
</head>
<body>
  <main class="flyer">
    <div class="brand">Terra Petro</div>
    <h1 class="headline-top">YOUR LOCAL CHOICE FOR</h1>
    <h2 class="headline-main">BULK FUEL SUPPLY!</h2>

    <svg class="hero" viewBox="0 0 570 600">
      <defs>
        <linearGradient id="photoTone" x1="0" y1="0" x2="1" y2="1">
          <stop offset="0" stop-color="#8a9098"/>
          <stop offset=".45" stop-color="#3a3d42"/>
          <stop offset="1" stop-color="#d9dadc"/>
        </linearGradient>
      </defs>
      <path d="M0 374 C200 350 400 325 570 319 V534 C500 480 420 440 300 420 C180 405 80 398 0 397 Z" fill="var(--red)"/>
      <path d="M390 404 C460 408 520 418 570 432" stroke="var(--white)" stroke-width="7" fill="none"/>
      <path d="M0 226 H480 L505 250 V418 C505 434 490 438 470 437 C330 430 160 390 0 372 Z"
            fill="url(#photoTone)" role="img"
            aria-label="Photo of a white road-train fuel tanker truck leaving a depot shed"/>
    </svg>

    <div class="service service--fuel">
      <div class="service-bar">BULK FUEL DELIVERIES.</div>
      <div class="service-icon">
        <svg width="14" height="18" viewBox="0 0 16 20"><rect x="1" y="1" width="14" height="18" rx="3" fill="#fff"/><path d="M1 7H15M1 13H15" stroke="#e8281e" stroke-width="1.5"/></svg>
      </div>
    </div>
    <div class="service service--oils">
      <div class="service-bar">OILS &amp; LUBRICANTS.</div>
      <div class="service-icon">
        <svg width="14" height="18" viewBox="0 0 16 20"><path d="M8 1 C11 6 15 10 15 13 A7 7 0 0 1 1 13 C1 10 5 6 8 1 Z" fill="none" stroke="#fff" stroke-width="2"/><path d="M5 13 A3 3 0 0 0 8 16" stroke="#fff" stroke-width="2" fill="none"/></svg>
      </div>
    </div>
    <div class="service service--family">
      <div class="service-bar">LOCAL FAMILY OWNED BUSINESS.</div>
      <div class="service-icon">
        <svg width="18" height="16" viewBox="0 0 20 18"><path d="M2 9 L10 2 L18 9 M4 8 V17 H16 V8" fill="none" stroke="#fff" stroke-width="2" stroke-linejoin="round"/></svg>
      </div>
    </div>

    <p class="cta"><strong>NEED FUEL DELIVERED?</strong> Call Your Local Team</p>

    <section class="team">
      <div class="contact contact--marco">
        <div class="contact-name">Marco</div>
        <div class="contact-phone">0400 000 001</div>
        <div class="contact-email">mtorrisi@terrapetro-example.com.au</div>
      </div>
      <div class="contact contact--liam">
        <div class="contact-name">Liam</div>
        <div class="contact-phone">0400 000 002</div>
        <div class="contact-email">lharcourt@terrapetro-example.com.au</div>
      </div>
      <div class="contact contact--peter">
        <div class="contact-name">Peter</div>
        <div class="contact-phone">0400 000 003</div>
        <div class="contact-email">pwinslow@terrapetro-example.com.au</div>
      </div>
    </section>

    <footer class="footer">
      <span class="footer-office">Office: 02 5550 0100</span>
      <div class="footer-call">
        <svg width="28" height="28" viewBox="0 0 24 24"><path d="M6.6 10.8c1.4 2.8 3.8 5.1 6.6 6.6l2.2-2.2c.3-.3.7-.4 1-.2 1.1.4 2.3.6 3.6.6.6 0 1 .4 1 1V20c0 .6-.4 1-1 1C10.6 21 3 13.4 3 4c0-.6.4-1 1-1h3.5c.6 0 1 .4 1 1 0 1.3.2 2.5.6 3.6.1.3 0 .7-.2 1z" fill="#fff"/><path d="M14 3a7 7 0 0 1 7 7M14 6.5a3.5 3.5 0 0 1 3.5 3.5" stroke="#fff" stroke-width="1.8" fill="none" stroke-linecap="round"/></svg>
      </div>
      <span class="footer-email">Fuel@terrapetro-example.com.au</span>
    </footer>
  </main>
</body>
</html>
```